Updating our Raw Materials Brochure

Please update and modify (to add more space for the additional text) the brochure designed for us in January (see attached file) so we can circulate a May 2021 version. Thanks and hope your family is OK despite the terrible tragedy going on with Covid-19 in India. Best wishes!

```html
<!DOCTYPE html>
<html lang="en">
<head>
<meta charset="utf-8">
<title>Raw Materials – May 2021 Market Update</title>
<link rel="stylesheet" href="https://fonts.googleapis.com/css2?family=Montserrat:wght@600;700&family=Titillium+Web:wght@600;700&family=Open+Sans:wght@400;600;700&display=swap">
<style>
  :root{
    --red:#e3141d;
    --ink:#14161b;
    --blue:#5a7fba;
    --blue-dark:#3c5f98;
    --panel:#efefef;
    --text:#333;
    --orange:#f07a22;
    --chart-blue:#3e6fc0;
    --backdrop:#d9d9d9;
  }
  *{box-sizing:border-box;margin:0;padding:0}
  html,body{width:1200px;height:834px;overflow:hidden}
  body{background:var(--backdrop);font-family:"Open Sans",sans-serif;color:var(--text);position:relative}
  .page{position:absolute;top:102px;width:481px;height:623px;background:#fff;overflow:hidden;box-shadow:0 2px 6px rgba(0,0,0,.18)}
  .page--front{left:105px}
  .page--back{left:625px;background:var(--panel)}
  .abs{position:absolute}
  .hero{position:absolute;left:0;width:481px;background:linear-gradient(100deg,#1a1d22 0%,#2d3640 35%,#1d232a 60%,#3a434c 80%,#15171b 100%)}
  .hero-title{position:absolute;left:0;width:481px;text-align:center;font-family:"Montserrat",sans-serif;font-weight:700;color:#fff;line-height:1}
  .hero-title--main{font-size:34px;letter-spacing:.5px}
  .hero-title--sub{font-size:22px;letter-spacing:11px;color:var(--red);padding-left:11px}
  .brand{font-family:"Montserrat",sans-serif;font-weight:700;display:flex;align-items:center;gap:6px;font-size:15px;letter-spacing:.5px}
  .brand-dot{width:14px;height:14px;border-radius:50%;background:currentColor}
  .band{position:absolute;background:var(--red)}
  .contact{right:20px;top:31px;text-align:right;font-family:"Montserrat",sans-serif;font-weight:700}
  .contact-label{color:var(--red);font-size:11px}
  .contact-phone{color:var(--ink);font-size:14.5px;margin-top:3px;display:flex;align-items:center;gap:4px;justify-content:flex-end}
  .section-head{position:absolute;background:var(--blue);color:#fff;font-family:"Titillium Web",sans-serif;font-weight:700;text-transform:uppercase}
  .section-head--angled{clip-path:polygon(0 0,94% 0,100% 100%,0 100%)}
  .section-head--plain{text-transform:none;font-family:"Open Sans",sans-serif;text-align:center}
  .section-edge{position:absolute;background:#444;clip-path:polygon(0 0,94% 0,100% 100%,0 100%)}
  .copy{position:absolute;font-size:6.4px;line-height:8.4px;text-align:justify}
  .copy p+p{margin-top:7px}
  .subhead{position:absolute;color:var(--red);font-family:"Titillium Web",sans-serif;font-weight:700;font-size:8.2px;text-align:center;line-height:8.5px;text-transform:uppercase}
  .panel{position:absolute;background:var(--panel)}
  .foot{position:absolute;left:0;bottom:0;width:481px;height:11px;background:var(--blue)}
  .chart-box{position:absolute;background:#fff}
  svg text{font-family:"Open Sans",sans-serif}
</style>
</head>
<body>

<section class="page page--front">
  <div class="brand abs" style="left:26px;top:42px;color:var(--ink)"><span class="brand-dot"></span>KESTREL ADHESIVES</div>
  <div class="contact abs">
    <div class="contact-label">Call us at</div>
    <div class="contact-phone">
      <svg width="10" height="12" viewBox="0 0 10 12"><path d="M3 1 L1 2 C0 6 3 11 8 11 L9 9 L7 7 L6 8 C4 7 3 6 3 4 L4 3 Z" fill="var(--ink)"/></svg>
      800-555-0142
    </div>
  </div>
  <div class="band" style="left:252px;top:69px;width:229px;height:13px;clip-path:polygon(3% 0,100% 0,100% 100%,0 100%)"></div>
  <div class="hero" style="top:81px;height:140px" role="img" aria-label="Industrial pipework photograph in dark blue-grey tones"></div>
  <div class="hero-title hero-title--main" style="top:104px">RAW MATERIALS</div>
  <div class="hero-title hero-title--main" style="top:143px">MAY 2021</div>
  <div class="hero-title hero-title--sub" style="top:181px">MARKET UPDATE</div>
  <div class="band" style="left:0;top:221px;width:236px;height:12px;clip-path:polygon(0 0,100% 0,97% 100%,0 100%)"></div>

  <div class="panel" style="left:240px;top:233px;width:241px;height:380px"></div>

  <div class="section-edge" style="left:0;top:244px;width:198px;height:23px"></div>
  <div class="section-head section-head--angled" style="left:0;top:244px;width:192px;height:23px;font-size:16px;line-height:23px;padding-left:15px">Global Shortages</div>
  <div class="section-head" style="left:240px;top:244px;width:241px;height:23px;font-size:16px;line-height:23px;text-align:center">Key Constraints</div>

  <div class="copy" style="left:15px;top:272px;width:212px">
    <p>As the recovery builds momentum more manufacturers are trying to buy extra material to prevent running out. Nearly all inputs are affected and there seems to be no end in sight as supply is unable to keep up with demand.</p>
    <p>The situation has been complicated by a growing list of disasters. Starting with the deep freeze and blackouts wiping out energy and petrochemicals operations in February, the Suez canal back up in March then hackers bringing down the largest US pipeline this month.</p>
    <p>US GDP increased at a 10.7% annual rate or $554.2 billion in current dollars (adjusted to 6.4% for inflation) in the first quarter. Demand seems to be driven by personal income growing $2.4 trillion (up 59%) from increased government social benefits and pandemic relief programs. Expectations are it will continue as personal savings were $4.12 trillion (up 83% the fourth quarter) driving personal savings to 21%.</p>
    <p>The trailing 12-month Producer Price Index and Consumer Price Index were up 6.2% and 4.2% respectively. These should go higher as the trailing 4-months averages are 10.2% and 6.3% respectively. Our procurement team is focused on leveraging our global supply position and growing demand so we will continue to deliver you the most competitive costs available despite these conditions.</p>
  </div>

  <svg class="abs" style="left:15px;top:503px" width="212" height="106" viewBox="0 0 212 106">
    <text x="4" y="5" font-size="3.4" font-weight="700" fill="#333">Chart 2. 12-month percent change in consumer prices, Apr 2020 – Apr 2021</text>
    <text x="4" y="9" font-size="3" fill="#555">Percent change</text>
    <g stroke="#ddd" stroke-width=".4">
      <line x1="14" y1="14" x2="208" y2="14"/><line x1="14" y1="34" x2="208" y2="34"/>
      <line x1="14" y1="54" x2="208" y2="54"/><line x1="14" y1="74" x2="208" y2="74"/>
    </g>
    <line x1="14" y1="94" x2="208" y2="94" stroke="#888" stroke-width=".5"/>
    <g font-size="3.4" fill="#444" text-anchor="end">
      <text x="11" y="15">5</text><text x="11" y="35">4</text><text x="11" y="55">2</text><text x="11" y="75">1</text><text x="11" y="95">0</text>
    </g>
    <polyline fill="none" stroke="#c2306a" stroke-width=".7" points="20,67 35,70 50,70 65,64 80,63 95,63 110,65 125,65 140,65 155,66 170,64 185,61 200,36"/>
    <polyline fill="none" stroke="#5b54b8" stroke-width=".7" points="20,88 35,92 50,84 65,77 80,73 95,72 110,71 125,71 140,68 155,66 170,61 185,47 200,13"/>
    <g font-size="3.3" fill="#444" text-anchor="middle">
      <text x="20" y="99">Apr'20</text><text x="35" y="99">May</text><text x="50" y="99">Jun</text><text x="65" y="99">Jul</text><text x="80" y="99">Aug</text><text x="95" y="99">Sep</text><text x="110" y="99">Oct</text><text x="125" y="99">Nov</text><text x="140" y="99">Dec</text><text x="155" y="99">Jan</text><text x="170" y="99">Feb</text><text x="185" y="99">Mar</text><text x="200" y="99">Apr'21</text>
    </g>
    <rect x="45" y="101" width="130" height="5" fill="none" stroke="#bbb" stroke-width=".3"/>
    <line x1="50" y1="103.6" x2="62" y2="103.6" stroke="#5b54b8" stroke-width=".7"/>
    <text x="65" y="104.6" font-size="3.2" fill="#444">All items</text>
    <line x1="105" y1="103.6" x2="117" y2="103.6" stroke="#c2306a" stroke-width=".7"/>
    <text x="120" y="104.6" font-size="3.2" fill="#444">All items less food and energy</text>
  </svg>

  <div class="subhead" style="left:250px;top:274px;width:220px">Ethylene shortage drives prices higher</div>
  <div class="copy" style="left:254px;top:286px;width:211px">
    <p>Contractual prices for Ethylene (key feedstock for water based and hot melt adhesives) increased 56% from 2020 to a 7-year high of $0.47/lb in March as multiple severe weather cracker outages driven by the deep freeze in February forced 70% capacity offline. Restarting production has been difficult as so many sites were damaged simultaneously.</p>
  </div>

  <svg class="abs" style="left:254px;top:350px" width="212" height="124" viewBox="0 0 212 124">
    <text x="106" y="10" font-size="7" fill="#555" text-anchor="middle">Ethyelene, Contract and Spot Pricing</text>
    <g font-size="4.2" fill="#555" text-anchor="end">
      <text x="26" y="21">$0.650</text><text x="26" y="27.3">$0.600</text><text x="26" y="33.6">$0.550</text><text x="26" y="39.9">$0.500</text><text x="26" y="46.2">$0.450</text><text x="26" y="52.5">$0.400</text><text x="26" y="58.8">$0.350</text><text x="26" y="65.1">$0.300</text><text x="26" y="71.4">$0.250</text><text x="26" y="77.7">$0.200</text><text x="26" y="84">$0.150</text><text x="26" y="90.3">$0.100</text><text x="26" y="96.6">$0.050</text><text x="26" y="102.9">$0.000</text>
    </g>
    <line x1="30" y1="101" x2="208" y2="101" stroke="#ccc" stroke-width=".4"/>
    <polyline fill="none" stroke="var(--chart-blue)" stroke-width=".9" points="38,64 67,65 96,62 125,54 154,54 194,39"/>
    <polyline fill="none" stroke="var(--orange)" stroke-width=".9" points="38,70 67,71 96,67 125,51 154,51 194,29"/>
    <g font-size="4.4" fill="#555" text-anchor="middle">
      <text x="42" y="111">Oct-20</text><text x="74" y="111">Nov-20</text><text x="106" y="111">Dec-20</text><text x="138" y="111">Jan-21</text><text x="170" y="111">Feb-21</text><text x="200" y="111">Mar-21</text>
    </g>
    <line x1="40" y1="120" x2="52" y2="120" stroke="var(--chart-blue)" stroke-width=".8"/>
    <text x="54" y="121.5" font-size="4" fill="#555">Meridian Data Contract NA Ethylene</text>
    <line x1="128" y1="120" x2="140" y2="120" stroke="var(--orange)" stroke-width=".8"/>
    <text x="142" y="121.5" font-size="4" fill="#555">Meridian Data Spot C2</text>
  </svg>

  <div class="subhead" style="left:250px;top:493px;width:220px">Vinyl Acetate Monomer (VAM) – Key Ingredient<br>for water based adhesives</div>
  <div class="copy" style="left:254px;top:518px;width:211px">
    <p>VAM shortages became severe following the February winter storm driving prices up 128% since Jan-2021. All three US suppliers (Norvale, Ambrex and Halden Chem) declared force majeure and all four production sites were shut down. They were stuck in varying stages of restarting and ramping up to full rates for nearly 3 months so supplies remain limited and that is expected to continue through Q2 with demand currently outstripping supply.</p>
  </div>

  <div class="foot"></div>
</section>

<section class="page page--back">
  <div class="hero" style="top:0;height:194px" role="img" aria-label="Industrial pipework photograph in dark blue-grey tones"></div>
  <div class="brand abs" style="left:0;width:481px;top:26px;justify-content:center;color:#fff"><span class="brand-dot"></span>KESTREL ADHESIVES</div>
  <div class="hero-title hero-title--main" style="top:73px">RAW MATERIALS</div>
  <div class="hero-title hero-title--main" style="top:112px">MAY 2021</div>
  <div class="hero-title hero-title--sub" style="top:152px">MARKET UPDATE</div>
  <div class="band" style="left:0;top:194px;width:236px;height:11px;clip-path:polygon(0 0,100% 0,97% 100%,0 100%)"></div>
  <div class="abs" style="left:0;top:205px;width:481px;height:418px;background:var(--panel)"></div>

  <div class="section-edge" style="left:0;top:213px;width:228px;height:45px"></div>
  <div class="section-head section-head--angled" style="left:0;top:213px;width:222px;height:45px;font-size:14px;line-height:17.5px;padding:5px 0 0 15px">Logistics Limitations<br>vs. Demand Growth</div>

  <div class="chart-box" style="left:252px;top:200px;width:216px;height:124px">
    <svg width="216" height="124" viewBox="0 0 216 124">
      <text x="108" y="8" font-size="6.5" fill="#444" text-anchor="middle">VAM Index</text>
      <g font-size="4" fill="#555" text-anchor="end">
        <text x="18" y="17">$2,300.0</text><text x="18" y="27">$2,100.0</text><text x="18" y="37">$1,900.0</text><text x="18" y="47">$1,700.0</text><text x="18" y="57">$1,500.0</text><text x="18" y="67">$1,300.0</text><text x="18" y="77">$1,100.0</text><text x="18" y="87">$900.0</text><text x="18" y="97">$700.0</text><text x="18" y="107">$500.0</text>
      </g>
      <polyline fill="none" stroke="var(--orange)" stroke-width="1" points="28,92 60,92 92,91.5 122,91.5 152,85 182,46 212,18"/>
      <g font-size="4.2" fill="#555" text-anchor="middle">
        <text x="34" y="116">Oct-20</text><text x="64" y="116">Nov-20</text><text x="94" y="116">Dec-20</text><text x="124" y="116">Jan-21</text><text x="154" y="116">Feb-21</text><text x="184" y="116">Mar-21</text><text x="208" y="116">Apr-21</text>
      </g>
      <line x1="75" y1="121.5" x2="90" y2="121.5" stroke="var(--orange)" stroke-width=".8"/>
      <text x="93" y="123" font-size="3.8" fill="#555">Petrix VAM FOB Spot Low ($/mt)</text>
    </svg>
  </div>

  <div class="copy" style="left:15px;top:271px;width:211px">
    <p>The ramp up in production of consumer and industrial goods while consumers still rely more on at home delivery or pick up from stores (which require more trucks and warehousing) has driven unprecedented logistics tightness.</p>
  </div>

  <svg class="abs" style="left:15px;top:311px" width="212" height="120" viewBox="0 0 212 120">
    <text x="0" y="5" font-size="5.2" font-weight="700" fill="#222">A Logistical Nightmare</text>
    <text x="0" y="11" font-size="4.6" fill="#333">Transport, storage and inventory costs are near record highs in the U.S.</text>
    <g font-size="3.8" fill="#333">
      <line x1="0" y1="16" x2="3" y2="13" stroke="#111" stroke-width=".8"/><text x="5" y="16.5">Transportation</text>
      <line x1="42" y1="16" x2="45" y2="13" stroke="#e0417a" stroke-width=".8"/><text x="47" y="16.5">Warehousing</text>
      <line x1="79" y1="16" x2="82" y2="13" stroke="#3aa0d8" stroke-width=".8"/><text x="84" y="16.5">Inventories</text>
    </g>
    <text x="207" y="27" font-size="3.8" fill="#333" text-anchor="end">100 index level*</text>
    <g font-size="3.8" fill="#333" text-anchor="end">
      <text x="207" y="45">75</text><text x="207" y="73">50</text><text x="207" y="101">25</text>
    </g>
    <line x1="2" y1="73" x2="200" y2="73" stroke="#f2c100" stroke-width=".8" stroke-dasharray="2 1.5"/>
    <text x="42" y="36" font-size="3.8" fill="#333">Expansion</text>
    <text x="92" y="89" font-size="3.8" fill="#333">Contraction</text>
    <polyline fill="none" stroke="#3aa0d8" stroke-width=".7" points="6,40 15,45 25,47 35,52 45,51 55,56 65,55 75,58 85,57 95,59 105,56 115,60 125,58 135,55 145,52 155,50 165,47 175,46 185,43 195,36"/>
    <polyline fill="none" stroke="#e0417a" stroke-width=".7" points="6,45 15,42 25,48 35,45 45,53 55,50 65,58 75,52 85,60 95,55 105,61 115,54 125,60 135,50 145,54 155,44 165,49 175,40 185,42 195,34"/>
    <polyline fill="none" stroke="#111" stroke-width=".8" points="6,33 14,31 22,40 30,48 38,46 46,56 54,52 62,72 70,68 78,74 86,76 94,70 102,80 110,66 118,72 126,58 134,70 142,84 150,68 158,62 166,44 174,36 182,34 190,30 198,28"/>
    <g font-size="4" fill="#333" text-anchor="middle">
      <text x="40" y="108">2019</text><text x="132" y="108">2020</text><text x="190" y="108">2021</text>
    </g>
    <text x="0" y="114" font-size="3.4" fill="#555">Source: Freight Conditions Index</text>
    <text x="0" y="118.5" font-size="3.4" fill="#555">*The index is a diffusion index where 50 is the line between growth and contraction.</text>
  </svg>

  <div class="copy" style="left:15px;top:444px;width:211px">
    <p>Capacity is constrained by slowed construction in vehicles (chips and other materials shortages) as traditional channels are idled (shopping malls, etc.). Spot Van rates were up 58.1% versus April 2020 as outages cause chain reactions. Currently there is a traffic jam of 771 barges accumulated on the lower Mississippi due to a fractured bridge, so expectations are this will continue until year end.</p>
  </div>

  <svg class="abs" style="left:22px;top:507px" width="200" height="104" viewBox="0 0 200 104">
    <text x="100" y="5" font-size="3.6" font-weight="700" fill="#222" text-anchor="middle">Transportation Prices</text>
    <g fill="var(--chart-blue)">
      <rect x="2" y="41" width="3.6" height="54"/><rect x="8.5" y="43" width="3.6" height="52"/><rect x="15" y="42" width="3.6" height="53"/><rect x="21.5" y="43" width="3.6" height="52"/><rect x="28" y="42" width="3.6" height="53"/><rect x="34.5" y="44" width="3.6" height="51"/><rect x="41" y="42" width="3.6" height="53"/><rect x="47.5" y="45" width="3.6" height="50"/><rect x="54" y="46" width="3.6" height="49"/><rect x="60.5" y="41" width="3.6" height="54"/><rect x="67" y="37" width="3.6" height="58"/><rect x="73.5" y="38" width="3.6" height="57"/><rect x="80" y="30" width="3.6" height="65"/><rect x="86.5" y="48" width="3.6" height="47"/><rect x="93" y="40" width="3.6" height="55"/><rect x="99.5" y="31" width="3.6" height="64"/><rect x="106" y="21" width="3.6" height="74"/><rect x="112.5" y="16" width="3.6" height="79"/><rect x="119" y="10" width="3.6" height="85"/><rect x="125.5" y="9" width="3.6" height="86"/><rect x="132" y="8" width="3.6" height="87"/><rect x="138.5" y="9" width="3.6" height="86"/><rect x="145" y="11" width="3.6" height="84"/><rect x="151.5" y="9" width="3.6" height="86"/><rect x="158" y="13" width="3.6" height="82"/><rect x="164.5" y="8" width="3.6" height="87"/><rect x="171" y="7" width="3.6" height="88"/><rect x="177.5" y="5" width="3.6" height="90"/>
    </g>
    <line x1="0" y1="95" x2="184" y2="95" stroke="#888" stroke-width=".4"/>
    <g font-size="2.6" fill="#444">
      <text transform="translate(3,101) rotate(-45)">Jan-19</text><text transform="translate(29,101) rotate(-45)">May-19</text><text transform="translate(55,101) rotate(-45)">Sep-19</text><text transform="translate(81,101) rotate(-45)">Jan-20</text><text transform="translate(107,101) rotate(-45)">May-20</text><text transform="translate(133,101) rotate(-45)">Sep-20</text><text transform="translate(159,101) rotate(-45)">Jan-21</text><text transform="translate(179,101) rotate(-45)">Apr-21</text>
    </g>
  </svg>

  <div class="section-head section-head--plain" style="left:240px;top:334px;width:237px;height:44px;font-size:11.5px;line-height:15px;padding-top:7px">Polyethylene and Polyurethane<br>Prices near record highs</div>

  <div class="copy" style="left:254px;top:385px;width:211px">
    <p>About 42% of US oil refining capacity went offline in February (~5.5m barrels/day) but it has recovered to over 86% by last week. The shortages this created downstream continue to create spot outages of critical inputs resulting in reduced operating rates at our suppliers.</p>
    <p>For example, Polyethylene polymers (critical in hot melt adhesives) increased 39% this year plus Benzene increased 10% in April and Polyether Polyols (key feedstock for polyurethanes) are on 75% sales allocation because of limited domestic materials and difficulty bringing in imports from marine transport shortages. As a result, the price index for rubbers and plastics is up 9% since January and is still rising.</p>
  </div>

  <div class="chart-box" style="left:252px;top:511px;width:216px;height:92px">
    <svg width="216" height="92" viewBox="0 0 216 92">
      <text x="4" y="6" font-size="4.4" font-weight="700" fill="#222">Statlane</text>
      <line x1="26" y1="4.6" x2="32" y2="4.6" stroke="#3c5f98" stroke-width=".7"/>
      <text x="34" y="5.8" font-size="2.8" fill="#555">Producer price index, rubber and plastics</text>
      <rect x="176" y="10" width="34" height="68" fill="#f6f2c8"/>
      <g stroke="#e5e5e5" stroke-width=".3">
        <line x1="18" y1="18" x2="210" y2="18"/><line x1="18" y1="32" x2="210" y2="32"/><line x1="18" y1="46" x2="210" y2="46"/><line x1="18" y1="60" x2="210" y2="60"/><line x1="18" y1="74" x2="210" y2="74"/>
      </g>
      <text transform="translate(7,52) rotate(-90)" font-size="2.6" fill="#555">Index</text>
      <polyline fill="none" stroke="#3c5f98" stroke-width=".6" points="20,72 30,71 40,70 48,66 58,58 66,56 76,58 86,55 96,52 104,50 114,51 124,48 134,50 144,47 152,46 160,46 168,47 176,48 184,46 192,42 198,38 204,28 209,14"/>
      <g font-size="2.6" fill="#555" text-anchor="middle">
        <text x="30" y="82">2016</text><text x="60" y="82">2017</text><text x="90" y="82">2018</text><text x="120" y="82">2019</text><text x="150" y="82">2020</text><text x="180" y="82">2020</text><text x="205" y="82">2021</text>
      </g>
      <text x="4" y="89" font-size="2.4" fill="#777">Shaded area indicates recession</text>
      <text x="84" y="89" font-size="2.4" fill="#777">Source: labor statistics</text>
    </svg>
  </div>

  <div class="foot"></div>
</section>

</body>
</html>
```